Quorvane copiers needs flyer for the Melbourne B2B expo

A flyer to hand out had the business to Business expo in Melbourne. I am am happy with the layout attached , but i need a claen ( no watermarks) background for the top half of the fist page. It must have one of the copiers attached in the photo

```html
<!DOCTYPE html>
<html lang="en">
<head>
<meta charset="utf-8">
<title>Quorvane Copiers – Melbourne B2B Expo Flyer</title>
<link rel="stylesheet" href="https://fonts.googleapis.com/css2?family=Roboto+Condensed:wght@400;700&family=Roboto:ital,wght@0,400;0,700;1,700&display=swap">
<style>
  :root {
    --bg: #000000;
    --paper: #ffffff;
    --navy: #34496b;
    --navy-dark: #2b3d5c;
    --red: #e8242b;
    --orange: #f26a2a;
    --ink: #1e1e1e;
    --link: #f4792c;
  }
  * { box-sizing: border-box; margin: 0; padding: 0; }
  html, body { width: 1200px; height: 2250px; overflow: hidden; background: var(--bg); }
  body { position: relative; font-family: "Roboto Condensed", Arial, sans-serif; color: var(--ink); }

  .page { position: absolute; left: 190px; width: 821px; background: var(--paper); overflow: hidden; }
  .page--front { top: 48px; height: 1062px; }
  .page--back { top: 1137px; height: 1064px; }

  .abs { position: absolute; }

  /* front */
  .office-photo { left: 0; top: 0; width: 821px; height: 560px;
    background: linear-gradient(160deg, #dfe6ea 0%, #f3f6f7 45%, #cfd9dc 75%, #e9eef0 100%); }
  .copier-photo { background: linear-gradient(180deg, #c9ccd2 0%, #eef0f2 18%, #e2e4e7 60%, #f5f6f7 100%); border-radius: 6px; }
  .front-copier { left: 507px; top: 207px; width: 220px; height: 405px; }
  .brand { right: 36px; top: 44px; text-align: right; font-weight: 700;
    color: var(--navy-dark); font-size: 56px; line-height: 1; letter-spacing: 0.5px; }
  .brand span { display: block; }
  .swoosh { left: 0; top: 470px; }
  .promo-badge { left: 91px; top: 363px; width: 246px; height: 246px; border-radius: 50%;
    border: 8px solid var(--navy); background: radial-gradient(circle at 40% 35%, #f2552c, var(--red) 70%);
    display: flex; flex-direction: column; justify-content: center; align-items: center; text-align: center;
    color: #fff; font-family: "Roboto", sans-serif; font-style: italic; font-weight: 700; font-size: 17px; line-height: 1.25; gap: 10px; }
  .headline { left: 0; width: 821px; top: 626px; text-align: center; font-weight: 700; font-size: 34px; color: var(--navy); letter-spacing: 0.5px; }

  .plan { top: 681px; width: 233px; height: 291px; background: linear-gradient(180deg, #e8e8e9, #f7f7f7 40%, #efeff0); }
  .plan__tab { position: absolute; left: 18px; right: 18px; top: 0; height: 32px; background: linear-gradient(90deg, var(--red), var(--orange));
    clip-path: polygon(0 0, 100% 0, 94% 100%, 6% 100%); color: #fff; font-size: 17px; text-align: center; line-height: 32px; }
  .plan__price { position: absolute; left: 22px; top: 46px; color: var(--red); font-weight: 700; display: flex; align-items: flex-start; }
  .plan__price .cur { font-size: 26px; margin-top: 4px; }
  .plan__price .amt { font-size: 56px; line-height: 1; }
  .plan__price .unit { font-size: 12px; font-weight: 400; line-height: 1.2; margin: 18px 0 0 4px; }
  .plan__text { position: absolute; left: 22px; right: 8px; top: 118px; font-size: 15.5px; line-height: 1.27; color: var(--ink); white-space: nowrap; }
  .plan__text p + p { margin-top: 8px; }
  .plan__daily { position: absolute; right: 12px; bottom: 8px; text-align: right; color: var(--navy-dark); }
  .plan__daily .lead { font-size: 12px; display: block; }
  .plan__daily .val { display: flex; align-items: flex-end; justify-content: flex-end; }
  .plan__daily .val b { font-size: 34px; font-weight: 400; line-height: 1; }
  .plan__daily .val b sup { font-size: 18px; }
  .plan__daily .val small { font-size: 12px; line-height: 1.1; text-align: left; margin-left: 3px; }

  .ink-splash { background: linear-gradient(90deg, rgba(248,180,40,.55), rgba(232,60,40,.35) 25%, rgba(255,255,255,0) 45%, rgba(255,255,255,0) 70%, rgba(40,140,220,.6) 90%, rgba(20,110,200,.7)); }
  .front-splash { left: 0; top: 880px; width: 821px; height: 112px; }

  .footer-bar { left: 0; bottom: 0; width: 821px; height: 70px; background: var(--navy); color: #fff;
    font-family: "Roboto", sans-serif; font-size: 19px; display: flex; align-items: center; justify-content: center; gap: 6px; }
  .footer-bar b { font-weight: 700; }
  .footer-bar .web { color: var(--link); font-weight: 700; }

  /* back */
  .back-header { left: 0; top: 0; width: 821px; height: 150px; background: var(--navy); }
  .back-header p { position: absolute; right: 72px; top: 30px; width: 660px; text-align: right; color: #fff;
    font-weight: 700; font-size: 20.5px; line-height: 1.2; }
  .back-wave { left: 0; top: 90px; }
  .back-splash-top { left: 0; top: 150px; width: 400px; height: 100px;
    background: linear-gradient(90deg, rgba(250,190,40,.6), rgba(240,90,40,.45) 50%, rgba(255,255,255,0)); }
  .perks { left: 59px; top: 291px; list-style: none; }
  .perks li { width: 335px; height: 29px; margin-bottom: 11.5px; background: linear-gradient(90deg, var(--orange), var(--red) 30%);
    color: #fff; font-size: 20px; line-height: 29px; padding-left: 9px; }
  .back-copier-1 { left: 527px; top: 220px; width: 180px; height: 338px; }
  .back-copier-2 { left: 455px; top: 598px; width: 275px; height: 372px; }
  .features-tag { left: 60px; top: 587px; width: 155px; height: 32px; background: var(--navy);
    clip-path: polygon(0 0, 100% 0, 88% 100%, 0 100%); color: #fff; font-weight: 700; font-size: 22px; line-height: 32px; padding-left: 20px; }
  .features { left: 80px; top: 633px; list-style: none; font-size: 19px; line-height: 24px; color: var(--ink); }
  .features li { position: relative; padding-left: 18px; margin-bottom: 8px; }
  .features li::before { content: ""; position: absolute; left: 0; top: 10px; width: 5px; height: 5px; border-radius: 50%; background: var(--ink); }
  .back-splash-bottom { left: 0; top: 870px; width: 821px; height: 125px; }
</style>
</head>
<body>

<section class="page page--front">
  <div class="abs office-photo" role="img" aria-label="Bright office desk with a desktop computer, sofa and bookshelf"></div>

  <div class="abs brand"><span>QUORVANE</span><span>COPIERS</span></div>

  <svg class="abs swoosh" width="821" height="120" viewBox="0 0 821 120" aria-hidden="true">
    <path d="M0 60 C 200 20, 450 20, 821 70 L 821 120 L 0 120 Z" fill="#ffffff"/>
    <path d="M0 58 C 200 18, 450 18, 821 68" fill="none" stroke="#e8242b" stroke-width="6"/>
    <path d="M0 80 C 220 30, 470 40, 821 92 L 821 100 C 470 54, 220 46, 0 96 Z" fill="#34496b"/>
  </svg>

  <div class="abs copier-photo front-copier" role="img" aria-label="Free-standing A3/A4 colour copier with paper drawers"></div>

  <div class="abs promo-badge">
    <span>Free Standing A3/A4<br>Colour Printer</span>
    <span>Include All Toner &amp;<br>Service</span>
    <span>Change plans to suit<br>your needs</span>
  </div>

  <h1 class="abs headline">NO LOCK-IN CONTRACTS</h1>

  <div class="abs ink-splash front-splash" role="img" aria-label="Swirls of coloured ink in yellow, red and blue"></div>

  <article class="abs plan" style="left:45px">
    <div class="plan__tab">Small Business Plan</div>
    <div class="plan__price"><span class="cur">$</span><span class="amt">150</span><span class="unit">+GST<br>Per Month</span></div>
    <div class="plan__text"><p>Includes printer &amp; 3000 B&amp;W<br>pages p/m</p><p>Excess B&amp;W pages are<br>5c +GST and colour pages<br>are 9c +GST</p></div>
    <div class="plan__daily"><span class="lead">Thats only</span><span class="val"><b><sup>$</sup>5</b><small>+GST<br>Per Day</small></span></div>
  </article>

  <article class="abs plan" style="left:292px">
    <div class="plan__tab">Medium Business Plan</div>
    <div class="plan__price"><span class="cur">$</span><span class="amt">210</span><span class="unit">+GST<br>Per Month</span></div>
    <div class="plan__text"><p>Includes printer &amp; 6000 B&amp;W<br>pages p/m.</p><p>Excess B&amp;W pages are<br>3.5c +GST and colour pages<br>are 9c +GST</p></div>
    <div class="plan__daily"><span class="lead">Thats just</span><span class="val"><b><sup>$</sup>7</b><small>+GST<br>Per Day</small></span></div>
  </article>

  <article class="abs plan" style="left:539px">
    <div class="plan__tab">Discounted Colour Plan</div>
    <div class="plan__price"><span class="cur">$</span><span class="amt">280</span><span class="unit">+GST<br>Per Month</span></div>
    <div class="plan__text"><p>Includes printer &amp; 6000 B&amp;W<br>pages p/m.</p><p>Excess B&amp;W pages are<br>3.5c +GST and colour pages<br>are 9c +GST</p></div>
    <div class="plan__daily"><span class="lead">Less Than</span><span class="val"><b><sup>$</sup>9.5</b><small>+GST<br>Per Day</small></span></div>
  </article>

  <footer class="abs footer-bar">Call <b>1800 555 019</b> or visit <span class="web">www.quorvanecopiers.com.au</span> and quote Melboure B2B</footer>
</section>

<section class="page page--back">
  <div class="abs back-header"><p>Other plans available for TV &amp; movie production companies, schools &amp;<br>construction sites, contact us for more information</p></div>
  <svg class="abs back-wave" width="821" height="90" viewBox="0 0 821 90" aria-hidden="true">
    <path d="M0 40 C 250 0, 520 90, 821 50 L 821 90 L 0 90 Z" fill="#ffffff"/>
    <path d="M0 40 C 250 0, 520 90, 821 50" fill="none" stroke="#e8242b" stroke-width="7"/>
  </svg>
  <div class="abs back-splash-top" role="img" aria-label="Swirl of yellow and orange ink"></div>

  <div class="abs ink-splash back-splash-bottom" role="img" aria-label="Swirls of coloured ink in yellow, red and blue"></div>

  <ul class="abs perks">
    <li>No Lock-in Contracts</li>
    <li>Free Network Assistance</li>
    <li>A3 Printing and Scaning</li>
    <li>Fax, Hole Punch &amp; Stapler Options</li>
    <li>Booklet making</li>
    <li>All this from as little as $5 a day</li>
  </ul>

  <div class="abs copier-photo back-copier-1" role="img" aria-label="Colour copier on a cabinet stand"></div>

  <div class="abs features-tag">FEATURES</div>
  <ul class="abs features">
    <li>Fantastic colour reproduction</li>
    <li>Upto 35 ppm</li>
    <li>Advanced LED printing system</li>
    <li>Banner &amp; Tidefast Printing</li>
    <li>Flexible media handling</li>
    <li>Self Encrypting Hard Drive with<br>Wipe Technology</li>
  </ul>

  <div class="abs copier-photo back-copier-2" role="img" aria-label="Large colour copier with finisher unit"></div>

  <footer class="abs footer-bar">Call <b>1800 555 019</b> or visit <span class="web">www.quorvanecopiers.com.au</span> and quote Melboure B2B</footer>
</section>

</body>
</html>
```